Accounting firm needing business card / letterhead designed
Marcus T. Elbering, CPA
marcus@fernquill.com
www.fernquill.com
482 N Harlow Ave Calderwick, OH 43719
419-555-0172

```html
<!DOCTYPE html>
<html lang="en">
<head>
<meta charset="utf-8">
<title>Fernquill Stationery</title>
<link href="https://fonts.googleapis.com/css2?family=Roboto:wght@400;500;700&display=swap" rel="stylesheet">
<style>
  :root {
    --navy: #262262;
    --green: #8dc63f;
    --paper: #ffffff;
    --ink: #6d6e71;
    --ink-dark: #3a3a3a;
    --backdrop: #e6e6ea;
    --rule: #9a9a9a;
  }
  * { box-sizing: border-box; margin: 0; padding: 0; }
  html, body { width: 1200px; height: 984px; overflow: hidden; }
  body {
    background: var(--backdrop);
    font-family: "Roboto", Arial, sans-serif;
    position: relative;
  }
  .sprites { position: absolute; width: 0; height: 0; }
  .icon { width: 8px; height: 8px; fill: var(--navy); flex: none; }

  /* Letterhead */
  .letterhead {
    position: absolute; left: 97px; top: 108px; width: 553px; height: 776px;
    background: var(--paper);
    box-shadow: 0 2px 10px rgba(0,0,0,.18);
  }
  .edge-stripe {
    position: absolute; left: 0; top: 0; bottom: 0; width: 18px;
    background: var(--navy);
  }
  .edge-stripe .accent {
    position: absolute; left: 0; width: 100%;
    background: var(--green);
    border-top: 3px solid var(--paper);
    border-bottom: 3px solid var(--paper);
  }
  .letterhead .edge-stripe .accent { top: 27px; height: 104px; }
  .wordmark {
    font-weight: 700; color: var(--navy); letter-spacing: 1px; line-height: 1;
  }
  .letterhead .wordmark { position: absolute; left: 47px; top: 60px; font-size: 34px; }
  .lh-contact {
    position: absolute; left: 396px; top: 49px;
    font-size: 9.5px; line-height: 13px; color: var(--ink-dark);
  }
  .lh-contact .address { margin-bottom: 5px; }
  .contact-row { display: flex; align-items: center; gap: 6px; }
  .addressee {
    position: absolute; left: 47px; top: 232px;
    font-size: 10px; line-height: 14.5px; color: var(--ink);
  }
  .letter-body {
    position: absolute; left: 47px; top: 319px; width: 459px;
    font-size: 10px; line-height: 14.5px; color: var(--ink);
    text-align: justify;
  }
  .letter-body p + p { margin-top: 28px; }
  .signature {
    position: absolute; left: 47px; top: 520px; width: 104px; height: 72px;
    background: linear-gradient(120deg, #ececf4, #dcdcec);
  }
  .signer-title {
    position: absolute; left: 47px; top: 608px;
    font-size: 10px; color: var(--ink);
  }

  /* Business cards */
  .card {
    position: absolute; left: 710px; width: 380px; height: 217px;
    box-shadow: 0 2px 10px rgba(0,0,0,.2);
  }
  .card-front { top: 251px; background: var(--paper); }
  .card-front .edge-stripe { width: 12px; }
  .card-front .edge-stripe .accent { top: 107px; height: 36px; }
  .card-front .wordmark { position: absolute; left: 25px; top: 32px; font-size: 30px; }
  .holder-name {
    position: absolute; left: 25px; top: 108px;
    font-size: 18px; font-weight: 500; color: var(--navy);
  }
  .holder-title {
    position: absolute; left: 25px; top: 131px;
    font-size: 12px; color: var(--ink-dark);
  }
  .card-rule {
    position: absolute; left: 25px; top: 148px; width: 332px;
    border-top: 1px solid var(--rule);
  }
  .card-contact {
    position: absolute; left: 25px; top: 159px;
    font-size: 9.5px; line-height: 13px; color: var(--ink-dark);
  }
  .card-address {
    position: absolute; right: 24px; top: 172px; text-align: right;
    font-size: 9.5px; line-height: 12.5px; color: var(--ink-dark);
  }
  .card-back { top: 510px; background: var(--navy); color: var(--paper); text-align: center; }
  .card-back .wordmark { position: absolute; left: 0; right: 0; top: 84px; font-size: 38px; color: var(--paper); }
  .card-back .site { position: absolute; left: 0; right: 0; top: 183px; font-size: 10px; }
</style>
</head>
<body>
  <svg class="sprites" aria-hidden="true">
    <symbol id="i-phone" viewBox="0 0 16 16"><path d="M3.6 1.2l2.2 2.7c.3.4.3.9 0 1.3L4.7 6.5c.9 1.9 2.8 3.9 4.8 4.8l1.3-1.1c.4-.3.9-.3 1.300l2.7 2.2c.4.3.4.9.1 1.3l-1.2 1.2C11.2 16.4 0 5.2 1.1 2.5L2.3 1.3c.4-.4 1-.4 1.3-.1z"/></symbol>
    <symbol id="i-mail" viewBox="0 0 16 16"><path d="M1 3h14v1.6L8 9 1 4.6z"/><path d="M1 6.4l7 4.3 7-4.3V13H1z"/></symbol>
    <symbol id="i-globe" viewBox="0 0 16 16"><path d="M8 1a7 7 0 100 14A7 7 0 008 1zm0 1.5c.8 0 1.7 1.4 2 3.5H6c.3-2.1 1.2-3.5 2-3.5zM5.8 7.5h4.4a12 12 0 010 1H5.8a12 12 0 010-1zM2.6 7.5h1.7v1H2.6a5.6 5.6 0 010-1zm9.1 0h1.7a5.6 5.6 0 010 1h-1.7zM6 10h4c-.3 2.1-1.2 3.5-2 3.5S6.3 12.1 6 10zM3 6a5.5 5.5 0 012.9-3.1A8 8 0 004.6 6zm8.4 0a8 8 0 00-1.3-3.1A5.5 5.5 0 0113 6zM3 10h1.6a8 8 0 001.3 3.1A5.5 5.5 0 013 10zm7.1 3.1a8 8 0 001.3-3.1H13a5.5 5.5 0 01-2.9 3.1z"/></symbol>
  </svg>

  <section class="letterhead">
    <div class="edge-stripe"><div class="accent"></div></div>
    <div class="wordmark">FERNQUILL</div>
    <div class="lh-contact">
      <div class="address">482 N Harlow Ave Calderwick<br>OH 43719</div>
      <div class="contact-row"><svg class="icon"><use href="#i-phone"/></svg>555-555-0172</div>
      <div class="contact-row"><svg class="icon"><use href="#i-mail"/></svg>marcus@fernquill.com</div>
      <div class="contact-row"><svg class="icon"><use href="#i-globe"/></svg>www.fernquill.com</div>
    </div>
    <div class="addressee">
      Dear Halvorsen<br>Orrin Paper Works Corporation<br>Department Design
    </div>
    <div class="letter-body">
      <p>Lorem ipsum dolor sit amet, consectetuer adipiscing elit. Aenean commodo ligula eget dolor. Aenean massa. Cum sociis natoque penatibus et magnis dis parturient montes, nascetur ridiculus mus. Donec quam felis, ultricies nec, pellentesque eu, pretium quis, sem. Nulla consequat massa quis enim. Donec pede justo, fringilla vel, aliquet nec, vulputate eget, arcu. In enim justo, rhoncus ut, imperdiet a, venenatis vitae, justo. Nullam dictum felis eu pede mollis pretium. Integer tincidunt. Cras dapibus. Vivamus elementum semper nisi.Nullam dictum felis eu pede mollis pretium. Integer tincidunt. Cras dapibus. Vivamus elementum semper nisi.felis eu pede mollis pretium. Integer tincidunt. Cras dapibus.</p>
      <p>Quisque rutrum. Aenean imperdiet. Etiam ultricies nisi vel augue. Curabitur ullamcorper ultricies nisi. Nam eget dui. Etiam rhoncus. Maecenas tempus, tellus eget condimentum rhoncus, sem quam semper libero, sit amet adipiscing sem neque sed ipsum.felis pede mollis pretium. I am tincidunt. Cras dapibus.</p>
    </div>
    <div class="signature" role="img" aria-label="Handwritten signature of the director"></div>
    <div class="signer-title">Director/Excecutive Director</div>
  </section>

  <section class="card card-front">
    <div class="edge-stripe"><div class="accent"></div></div>
    <div class="wordmark">FERNQUILL</div>
    <div class="holder-name">Marcus T. Elbering</div>
    <div class="holder-title">CPA</div>
    <div class="card-rule"></div>
    <div class="card-contact">
      <div class="contact-row"><svg class="icon"><use href="#i-phone"/></svg>555-555-0172</div>
      <div class="contact-row"><svg class="icon"><use href="#i-mail"/></svg>marcus@fernquill.com</div>
      <div class="contact-row"><svg class="icon"><use href="#i-globe"/></svg>www.fernquill.com</div>
    </div>
    <div class="card-address">482 N Harlow Ave Calderwick<br>OH 43719</div>
  </section>

  <section class="card card-back">
    <div class="wordmark">FERNQUILL</div>
    <div class="site">www.fernquill.com</div>
  </section>
</body>
</html>
```